A Health & Fitness Website selling saunas and Cold tubs

www.tarnwellgear.com, www.frostvaleco, www.brimholdsupply
Design a website
We are selling saunas, infrared saunas, cold plunge tubs, and massage chairs to financially successful MEN.
We want professional, simple, masculine with a touch of sexy.
One section for each… saunas, cold plunge tubs, massage chairs.
Each will have at least two buy links to their affiliate/supplier/store.
The landing page / opening page / needs big & bold; a full screen image? a great picture showing the warmth of a sauna? Need your ideas
The pictures are everything.

The Website for our book
https://maplewickvigor.com/

Coding

Coded - Design and coding required

Number of Pages Required

1 page

Requirements
Must have
• Great pictures

```html
<!DOCTYPE html>
<html lang="en">
<head>
<meta charset="utf-8">
<title>Maplewick Vigor – Saunas, Cold Plunge Tubs &amp; Massage Chairs</title>
<link href="https://fonts.googleapis.com/css2?family=Oswald:wght@400;500;600;700&family=Montserrat:ital,wght@0,400;0,500;0,600;0,700;1,400;1,500&display=swap" rel="stylesheet">
<style>
:root{
  --orange:#dd4a1e;
  --orange-soft:#e86a3f;
  --ink:#1b1b1b;
  --dark:#141414;
  --grey-bg:#f5f5f5;
  --text:#4a4a4a;
  --white:#ffffff;
  --wood-1:#6b3a1c;
  --wood-2:#b8743d;
}
*{box-sizing:border-box;margin:0;padding:0}
html,body{width:1200px;height:4286px;overflow:hidden}
body{font-family:'Montserrat',sans-serif;color:var(--ink);background:var(--white);position:relative}
.abs{position:absolute}
.display{font-family:'Oswald',sans-serif;font-weight:600;text-transform:uppercase;letter-spacing:.5px}

/* hero */
.hero{position:absolute;left:0;top:0;width:1200px;height:700px;
  background:linear-gradient(100deg,#5a2e14 0%,#8f5428 35%,#b57440 60%,#7a4220 100%)}
.hero-shade{position:absolute;inset:0;background:linear-gradient(90deg,rgba(40,18,6,.55) 0%,rgba(40,18,6,.1) 60%)}
.brand{position:absolute;left:108px;top:20px;display:flex;align-items:center;gap:12px;color:var(--white);font-weight:700;font-size:18px;line-height:1.2}
.brand-dot{width:44px;height:44px;border-radius:50%;background:var(--white)}
.nav{position:absolute;top:58px;left:524px;display:flex;gap:33px;font-family:'Oswald',sans-serif;font-weight:500;font-size:18px;color:var(--white);text-transform:uppercase}
.nav .active{text-decoration:underline;text-underline-offset:5px}
.hero-title{position:absolute;left:110px;top:202px;font-size:60px;line-height:70px;color:var(--white);width:640px}
.hero-sub{position:absolute;left:110px;top:430px;width:560px;font-size:21px;line-height:32px;color:var(--white)}
.btn-light{position:absolute;left:111px;top:554px;width:273px;height:63px;border-radius:32px;background:var(--white);color:var(--ink);font-weight:500;font-size:19px;display:flex;align-items:center;justify-content:center}

/* circulation */
.circ{position:absolute;left:0;top:700px;width:1200px;height:820px;background:var(--grey-bg)}
.circ-title{position:absolute;left:602px;top:90px;font-size:51px;line-height:63px}
.circ-sub{position:absolute;left:602px;top:230px;font-family:'Oswald',sans-serif;font-size:41px;color:var(--ink)}
.circ-lead{position:absolute;left:602px;top:318px;font-weight:700;font-size:27px;line-height:40px;color:var(--orange)}
.benefits{position:absolute;top:466px;list-style:none;font-size:16px;color:var(--text)}
.benefits li{position:relative;padding-left:24px;margin-bottom:19px;line-height:20px}
.benefits li::before{content:"";position:absolute;left:2px;top:3px;width:6px;height:11px;border:solid var(--orange);border-width:0 3px 3px 0;transform:rotate(45deg)}
.col-a{left:602px}.col-b{left:835px;width:220px}

/* products */
.section-title{position:absolute;left:0;width:1200px;top:1596px;text-align:center;font-size:51px;line-height:64px}
.product h3{position:absolute;font-size:31px;font-weight:600}
.product .price{position:absolute;font-size:17px;color:var(--text)}
.product .desc{position:absolute;width:410px;font-size:16.5px;line-height:26.5px;color:var(--text)}
.btn{position:absolute;height:63px;border-radius:32px;color:var(--white);font-weight:600;font-size:19px;display:flex;align-items:center;justify-content:center;width:172px}
.btn-buy{background:var(--orange)}
.btn-store{background:var(--ink)}
.frame{position:absolute;border:2px solid var(--orange)}
.photo{position:absolute}

/* testimonial */
.testi{position:absolute;left:0;top:3183px;width:1200px;height:619px;background:var(--white)}
.testi-title{position:absolute;left:110px;top:82px;font-size:52px;line-height:62px;color:var(--white)}
.testi-quote{position:absolute;left:112px;top:244px;width:640px;font-style:italic;font-size:20.5px;line-height:34px;color:var(--white)}
.arrow{position:absolute;top:453px;width:43px;height:53px;display:flex;align-items:center;justify-content:center}
.arrow-prev{left:110px;background:var(--orange-soft)}
.arrow-next{left:163px;background:var(--white)}

/* footer */
.footer{position:absolute;left:0;top:3802px;width:1200px;height:484px;background:var(--dark);color:var(--white)}
.footer-brand{position:absolute;left:470px;top:170px;display:flex;align-items:center;gap:12px;font-weight:700;font-size:20px}
.footer-brand .brand-dot{width:40px;height:40px}
.sub-title{position:absolute;left:769px;top:106px;font-weight:600;font-size:19px}
.sub-input{position:absolute;left:769px;top:158px;width:346px;height:55px;background:var(--white);color:#555;font-size:15px;padding-left:18px;display:flex;align-items:center}
.sub-btn{position:absolute;left:769px;top:237px;width:143px;height:53px;border-radius:27px;background:var(--orange);font-weight:600;font-size:17px;display:flex;align-items:center;justify-content:center}
.rule{position:absolute;left:110px;top:376px;width:978px;height:1px;background:#3a3a3a}
.copy{position:absolute;left:110px;top:408px;font-size:16px}
.social{position:absolute;top:398px;width:42px;height:42px;border-radius:50%;border:2px solid var(--white)}
</style>
</head>
<body>

<header class="hero">
  <div role="img" aria-label="Photo of a man relaxing shirtless on the bench of a warm wooden sauna" class="hero-shade"></div>
  <div class="brand"><span class="brand-dot"></span><span>Maplewick Vigor</span></div>
  <nav class="nav">
    <span class="active">Home</span><span>Sauna</span><span>Cold Plunge Tubs</span><span>Massage Chairs</span><span>Contact</span>
  </nav>
  <h1 class="hero-title display">Dramatically Improve Your Health Without Exercise</h1>
  <p class="hero-sub">Successful Men Recognize the Importance of Their Health and Make it a Priority.&nbsp; It’s Your Time.&nbsp; You’ve Earned it.</p>
  <div class="btn-light">EXPLORE PRODUCTS</div>
</header>

<section class="circ">
  <svg class="abs" style="left:0;top:0" width="580" height="820" viewBox="0 0 580 820" role="img" aria-label="Photo of a fit couple posing together in black swimwear">
    <defs><linearGradient id="skin" x1="0" y1="0" x2="0" y2="1"><stop offset="0" stop-color="#b0714a"/><stop offset="1" stop-color="#7a4a2e"/></linearGradient></defs>
    <polygon points="243,0 575,0 335,820 0,820 0,0" fill="url(#skin)"/>
    <polygon points="243,0 575,0 335,820 200,820 300,340" fill="var(--orange)" opacity=".9"/>
  </svg>
  <h2 class="circ-title display">A Mans Body Thrives<br>on Circulation</h2>
  <p class="circ-sub">And It Doesn’t Care How You Get It</p>
  <p class="circ-lead">When there’s no time for exercise.<br>Use Hot, Cold, or Massage.<br>The Benefits are Numerous.</p>
  <ul class="benefits col-a">
    <li>Relieve Stress</li><li>Detox Your Pores</li><li>Sleep Better</li><li>Relieve Muscle Tension</li>
    <li>Boost Energy Levels</li><li>Increase Testosterone</li><li>Reduce Inflammation</li><li>Increase Immunity</li>
  </ul>
  <ul class="benefits col-b">
    <li>Reduce Depression</li><li>Alleviate Joint Pain</li><li>Healthier Skin</li><li>Lower the Risk of Cardiovascular Disease</li>
    <li>Increase Metabolism</li><li>Promote Weight Loss</li><li>A Longer &amp; Healthier Life</li>
  </ul>
</section>

<h2 class="section-title display">Specific Improvements Will Be<br>Individual to You</h2>

<article class="product">
  <div class="frame" style="left:839px;top:1769px;width:289px;height:303px"></div>
  <div class="photo" role="img" aria-label="Photo of a couple in white robes inside an infrared sauna" style="left:559px;top:1807px;width:530px;height:343px;background:linear-gradient(135deg,#c98a4e,#e8b27a 50%,#9a5e30)"></div>
  <h3 style="left:110px;top:1800px">Infrared Saunas</h3>
  <p class="price" style="left:110px;top:1854px">From $9,999.00 USD</p>
  <p class="desc" style="left:110px;top:1902px">Lorem ipsum dolor sit amet, consectetur adiping elit, sed do eiusmod tempor incididunt ut labore et dolore magna aliqua. Ut enim ad minim vlum, quis nostrud exercitation ullamco laboris nisi ut aliquip ex ea commodo con.</p>
  <div class="btn btn-buy" style="left:111px;top:2067px">BUY ONLINE</div>
  <div class="btn btn-store" style="left:291px;top:2067px">VISIT STORE</div>
</article>

<article class="product">
  <div class="frame" style="left:72px;top:2235px;width:289px;height:299px"></div>
  <div class="photo" role="img" aria-label="Photo of a cold plunge tub outside a modern house in the snow" style="left:111px;top:2271px;width:530px;height:343px;background:linear-gradient(180deg,#8c94c4,#b7bedf 55%,#6d6a80)"></div>
  <h3 style="left:691px;top:2265px">Cold plunge tubs</h3>
  <p class="price" style="left:691px;top:2319px">From $9,999.00 USD</p>
  <p class="desc" style="left:691px;top:2367px">Lorem ipsum dolor sit amet, consectetur adiping elit, sed do eiusmod tempor incididunt ut labore et dolore magna aliqua. Ut enim ad minim vlum, quis nostrud exercitation ullamco laboris nisi ut aliquip ex ea commodo con.</p>
  <div class="btn btn-buy" style="left:691px;top:2532px">BUY ONLINE</div>
  <div class="btn btn-store" style="left:871px;top:2532px">VISIT STORE</div>
</article>

<article class="product">
  <div class="frame" style="left:839px;top:2697px;width:289px;height:302px"></div>
  <div class="photo" role="img" aria-label="Photo of a cream and tan massage chair in a sunlit room" style="left:559px;top:2734px;width:530px;height:344px;background:linear-gradient(120deg,#efe3d2,#d9b08a 55%,#8a5a36)"></div>
  <h3 style="left:110px;top:2728px">Massage Chair</h3>
  <p class="price" style="left:110px;top:2782px">From $9,999.00 USD</p>
  <p class="desc" style="left:110px;top:2830px">Lorem ipsum dolor sit amet, consectetur adiping elit, sed do eiusmod tempor incididunt ut labore et dolore magna aliqua. Ut enim ad minim vlum, quis nostrud exercitation ullamco laboris nisi ut aliquip ex ea commodo con.</p>
  <div class="btn btn-buy" style="left:111px;top:2995px">BUY ONLINE</div>
  <div class="btn btn-store" style="left:291px;top:2995px">VISIT STORE</div>
</article>

<section class="testi">
  <svg class="abs" style="left:0;top:0" width="1200" height="619" viewBox="0 0 1200 619">
    <polygon points="0,0 929,0 690,619 0,619" fill="var(--orange)"/>
    <polygon points="929,0 1200,0 1200,619 690,619" fill="url(#ladyFill)" role="img" aria-label="Photo of a smiling fit woman in a white sports top"/>
    <defs><linearGradient id="ladyFill" x1="0" y1="0" x2="0" y2="1"><stop offset="0" stop-color="#e9d6b8"/><stop offset=".5" stop-color="#d49a72"/><stop offset="1" stop-color="#c2532a"/></linearGradient></defs>
  </svg>
  <h2 class="testi-title display">Everything Works Better With<br>Increased Blood Flow</h2>
  <p class="testi-quote">“I climb in my sauna half asleep every morning for 20 minutes before I take a shower and head off to work. It's the only thing I found that really wakes me up in the morning. I'm not a coffee drinker so that's never been an option but this sauna is the perfect morning wake up.”</p>
  <div class="arrow arrow-prev"><svg width="14" height="22" viewBox="0 0 14 22"><path d="M11 2 L3 11 L11 20" fill="none" stroke="#fff" stroke-width="2.5"/></svg></div>
  <div class="arrow arrow-next"><svg width="14" height="22" viewBox="0 0 14 22"><path d="M3 2 L11 11 L3 20" fill="none" stroke="#1b1b1b" stroke-width="2.5"/></svg></div>
</section>

<footer class="footer">
  <div class="abs" role="img" aria-label="Cover of the fitness book for men" style="left:125px;top:42px;width:208px;height:308px;background:linear-gradient(160deg,#e8e8e8,#c64a3a 40%,#8a1f22)"></div>
  <div class="footer-brand"><span class="brand-dot"></span><span>Maplewick Vigor</span></div>
  <p class="sub-title">SUBSCRIBE FOR UPDATES</p>
  <div class="sub-input">Email Address</div>
  <div class="sub-btn">SUBSCRIBE</div>
  <div class="rule"></div>
  <p class="copy">© Copyright - 2024, Maplewick Vigor Fitness for Men. All rights reserved.</p>
  <span class="social" style="left:993px" aria-label="Social profile"></span>
  <span class="social" style="left:1045px" aria-label="Social profile"></span>
</footer>

</body>
</html>
```